Personal Web page for recruiter and owner of consulting firm

I work full time as a recruiter so I want a page that allows for me to support my efforts. I would like a long single page, I need to be able to upload four two minute videos, and 4 images. I also want the color scheme to match with my consulting company. I own the domain marlowevantrees.com already through wordpress . I took a shot at it myself and its terrible.

Target Market(s)

Potential clients

Industry/Entity Type

Management Consulting

Logo Text

marlowe vantrees

Font styles to use
Serif

Requirements
Must have
• Must in color scheme go well with my consulting company logo attached
• Must be able to upload 4 two minute videos and 4 images (photos of me)
• Single long scroll page
• Modern and clean
Nice to have
• Easy for me to update videos images and text without complex coding
Should not have
• I want the design and feel to go well with my logos not exactly replicate it

```html
<!DOCTYPE html>
<html lang="en">
<head>
<meta charset="utf-8">
<title>Marlowe Vantrees</title>
<link rel="stylesheet" href="https://fonts.googleapis.com/css2?family=Jost:wght@400;500;600&family=Open+Sans:wght@400;600;700&display=swap">
<style>
:root{
  --blue:#2b58a5;
  --blue-dark:#1f4687;
  --ink:#333a44;
  --text:#5b6068;
  --muted:#8b9099;
  --line:#d5d8dd;
  --paper:#ffffff;
  --grey:#eef0f2;
  --footer:#3a3b3d;
}
*{box-sizing:border-box;margin:0;padding:0}
html,body{width:1200px;height:4286px;overflow:hidden}
body{position:relative;background:var(--paper);font-family:"Open Sans",sans-serif;color:var(--text)}
.abs{position:absolute}
.heading{font-family:"Jost",sans-serif;font-weight:400;letter-spacing:4px;color:var(--ink);text-transform:uppercase}
.heading b{font-weight:400;color:var(--blue)}
.rule{width:70px;height:3px;background:var(--blue);margin:14px auto 0}
.photo{position:absolute}

/* header */
.site-header{position:absolute;left:0;top:0;width:1200px;height:128px;background:var(--paper)}
.brand{position:absolute;left:96px;top:30px;display:flex;align-items:center;gap:10px}
.brand-ring{width:62px;height:62px;border:3px solid var(--blue);border-radius:50%}
.brand-name{font-family:"Jost",sans-serif;font-size:30px;font-weight:500;color:var(--blue);letter-spacing:2px;line-height:1}
.contact{position:absolute;top:64px;display:flex;align-items:center;gap:12px;font-size:18px;color:var(--ink)}
.menu{position:absolute;left:1066px;top:50px;width:40px;height:40px;border:2px solid var(--ink);border-radius:50%}
.menu i{position:absolute;left:11px;width:15px;height:2px;background:var(--ink)}

/* hero */
.hero{position:absolute;left:0;top:128px;width:1200px;height:507px;background:linear-gradient(90deg,#f4f6f8 0%,#e6ebf0 45%,#c9d4de 100%)}
.hero-text{position:absolute;left:98px;top:188px;font-family:"Open Sans",sans-serif;font-size:33px;line-height:42px;color:#4b4f55}
.hero-text strong{color:var(--blue);font-weight:700}

/* about */
.about{position:absolute;left:0;top:635px;width:1200px;text-align:center}
.about .heading{font-size:34px;margin-top:60px}
.about p{width:990px;margin:40px auto 0;font-size:14.5px;line-height:30px;color:var(--text)}

/* videos */
.band{position:absolute;left:0;top:987px;width:1200px;height:185px;background:var(--blue)}
.band h2{font-family:"Jost",sans-serif;font-weight:400;font-size:27px;color:#fff;letter-spacing:2px;text-align:center;margin-top:38px}
.video{position:absolute;width:516px;height:410px}
.play{position:absolute;left:50%;top:50%;width:64px;height:64px;margin:-32px 0 0 -32px}
.card{position:absolute;width:502px;height:277px;background:#f4f5f6;border-radius:4px;padding:28px 30px;box-shadow:0 2px 8px rgba(0,0,0,.12)}
.card h3{font-family:"Jost",sans-serif;font-weight:400;font-size:28px;letter-spacing:3px;color:var(--ink);text-transform:uppercase}
.card h3 b{font-weight:400;color:var(--blue)}
.card .bar{width:46px;height:3px;background:var(--blue);margin:8px 0 14px}
.card p{font-size:14.5px;line-height:27px;color:var(--text)}

/* expertise */
.expertise{position:absolute;left:0;top:2918px;width:1200px;height:427px;background:var(--grey)}
.expertise .heading{font-size:33px;text-align:center;margin-top:40px}
.expertise .rule{margin-top:10px}
.expertise-copy{position:absolute;left:100px;top:128px;width:650px;font-size:14.5px;line-height:29px}
.expertise ul{list-style:none;margin-top:22px}
.expertise li{font-size:13px;line-height:35px;padding-left:22px;position:relative}
.expertise li::before{content:"";position:absolute;left:0;top:12px;width:10px;height:10px;border-radius:50%;background:var(--blue)}

/* gallery */
.gallery{position:absolute;left:0;top:3345px;width:1200px;height:470px;background:linear-gradient(135deg,var(--blue) 0%,var(--blue-dark) 100%)}
.gallery h2{font-family:"Jost",sans-serif;font-weight:400;font-size:33px;letter-spacing:4px;color:#fff;text-align:center;margin-top:40px}
.gallery .rule{background:#fff;margin-top:10px}
.tile{position:absolute;top:143px;width:240px}
.tile .photo{position:relative;width:240px;height:172px;border:3px solid #fff}
.tile h4{font-family:"Jost",sans-serif;font-weight:500;font-size:17px;letter-spacing:1px;color:#fff;margin-top:16px}
.tile p{font-size:14px;line-height:25px;color:#c9d6ee;margin-top:4px}
.arrow{position:absolute;top:216px;width:20px;height:28px}

/* inquiry */
.inquiry{position:absolute;left:0;top:3815px;width:1200px;height:410px}
.inquiry .heading{position:absolute;left:100px;top:45px;font-size:33px}
.inquiry .lead{position:absolute;left:100px;top:118px;width:540px;font-size:17px;line-height:30px;color:var(--muted)}
.info{position:absolute;left:100px;display:flex;align-items:center;gap:18px;font-size:15px;color:var(--ink)}
.field{position:absolute;left:698px;width:402px;border:1px solid var(--line);font-size:13px;color:var(--ink);padding:10px 14px}
.submit{position:absolute;left:698px;top:310px;width:120px;height:43px;border:1px solid var(--blue);border-bottom-width:3px;background:#fff;color:var(--blue);font-family:"Open Sans",sans-serif;font-weight:700;font-size:15px;letter-spacing:1px}

/* footer */
.site-footer{position:absolute;left:0;top:4225px;width:1200px;height:61px;background:var(--footer);color:#c9cbce;font-size:13px}
.site-footer .copy{position:absolute;left:100px;top:22px}
.site-footer .copy b{color:#fff}
.follow{position:absolute;right:100px;top:16px;display:flex;align-items:center;gap:20px;font-size:17px}
.follow i{display:block;width:14px;height:14px;border-radius:50%;background:#e1e3e6}
</style>
</head>
<body>

<header class="site-header">
  <div class="brand"><div class="brand-ring"></div><div class="brand-name">MARLOWE VANTREES</div></div>
  <div class="contact" style="left:570px">
    <svg width="22" height="22" viewBox="0 0 24 24"><path fill="#2b58a5" d="M6.6 10.8a15 15 0 0 0 6.6 6.6l2.2-2.2a1 1 0 0 1 1-.25 11.4 11.4 0 0 0 3.6.57 1 1 0 0 1 1 1V20a1 1 0 0 1-1 1A17 17 0 0 1 3 4a1 1 0 0 1 1-1h3.5a1 1 0 0 1 1 1c0 1.25.2 2.45.57 3.6a1 1 0 0 1-.25 1z"/></svg>
    (014) 5550192
  </div>
  <div class="contact" style="left:765px">
    <svg width="26" height="20" viewBox="0 0 26 20"><rect x="1" y="1" width="24" height="18" rx="2" fill="#2b58a5"/><path d="M2 3l11 8 11-8" stroke="#fff" stroke-width="2" fill="none"/></svg>
    info@marlowevantrees.com
  </div>
  <div class="menu"><i style="top:12px"></i><i style="top:18px"></i><i style="top:24px;width:11px"></i></div>
</header>

<section class="hero" role="img" aria-label="Two colleagues smiling at a laptop in a bright office">
  <div class="photo" role="img" aria-label="Office scene with two recruiters at a laptop" style="left:640px;top:0;width:560px;height:507px;background:linear-gradient(160deg,#d4dde6 0%,#9fb3c7 50%,#e4e9ee 100%)"></div>
  <p class="hero-text"><strong>I SPECIALISE IN RECRUITING ROLES</strong><br>AT THE PROFESSIONAL CLERICAL<br>AND SUPPORT LEVELS.</p>
</section>

<section class="about">
  <h2 class="heading">About <b>Marlowe Vantrees</b></h2>
  <div class="rule"></div>
  <p>Lorem ipsum dolor sit amet, consectetuer adipiscing elit, sed diam nonummy nibh euismod tincidunt ut laoreet dolore magna aliquam erat volutpat. Ut wisi enim ad minim veniam, quis nostrud exerci tation ullamcorper suscipit lobortis nisl ut aliquip ex ea commodo consequat. Duis autem vel eum iriure dolor in hendrerit in vulputate velit esse molestie consequat, vel illum dolore eu feugiat nulla facilisis at vero eros et accumsan et iusto odio dignissim qui blandit praesent luptatum zzril delenit augue duis.</p>
</section>

<section class="band"><h2>Lorem Ipsum Dolor, Consectetuer Adipiscing, Diam Nonummy Euismod</h2></section>

<!-- video row 1 -->
<div class="video photo" role="img" aria-label="Video still: colleagues in discussion" style="left:117px;top:1080px;background:linear-gradient(135deg,#6d6f73,#3d3f44)">
  <svg class="play" viewBox="0 0 64 64"><circle cx="32" cy="32" r="29" fill="none" stroke="#fff" stroke-width="3"/><path d="M26 20l18 12-18 12z" fill="#fff"/></svg>
</div>
<article class="card" style="left:583px;top:1143px"><h3>Consectetuer <b>Adipiscing</b></h3><div class="bar"></div><p>Lorem ipsum dolor sit amet, consectetuer adipiscing elit, sed diam nonummy nibh euismod tincidunt ut laoreet dolore magna aliquam erat volutpat. Ut wisi enim ad minim veniam, quis nostrud exerci tation ullamcorper suscipit lobortis nisl ut aliquip ex ea commodo consequat. Duis autem vel eum iriure dolor in hendrerit in vulputate ve</p></article>

<!-- video row 2 -->
<div class="video photo" role="img" aria-label="Video still: team meeting around a table" style="left:571px;top:1535px;background:linear-gradient(135deg,#4a4d52,#2d2f33)">
  <svg class="play" viewBox="0 0 64 64"><circle cx="32" cy="32" r="29" fill="none" stroke="#fff" stroke-width="3"/><path d="M26 20l18 12-18 12z" fill="#fff"/></svg>
</div>
<article class="card" style="left:118px;top:1600px"><h3>Consectetuer <b>Adipiscing</b></h3><div class="bar"></div><p>Lorem ipsum dolor sit amet, consectetuer adipiscing elit, sed diam nonummy nibh euismod tincidunt ut laoreet dolore magna aliquam erat volutpat. Ut wisi enim ad minim veniam, quis nostrud exerci tation ullamcorper suscipit lobortis nisl ut aliquip ex ea commodo consequat. Duis autem vel eum iriure dolor in hendrerit in vulputate ve</p></article>

<!-- video row 3 -->
<div class="video photo" role="img" aria-label="Video still: business people talking" style="left:117px;top:1995px;background:linear-gradient(135deg,#3f4145,#26282b)">
  <svg class="play" viewBox="0 0 64 64"><circle cx="32" cy="32" r="29" fill="none" stroke="#fff" stroke-width="3"/><path d="M26 20l18 12-18 12z" fill="#fff"/></svg>
</div>
<article class="card" style="left:583px;top:2058px"><h3>Consectetuer <b>Adipiscing</b></h3><div class="bar"></div><p>Lorem ipsum dolor sit amet, consectetuer adipiscing elit, sed diam nonummy nibh euismod tincidunt ut laoreet dolore magna aliquam erat volutpat. Ut wisi enim ad minim veniam, quis nostrud exerci tation ullamcorper suscipit lobortis nisl ut aliquip ex ea commodo consequat. Duis autem vel eum iriure dolor in hendrerit in vulputate ve</p></article>

<!-- video row 4 -->
<div class="video photo" role="img" aria-label="Video still: handshake across a desk" style="left:571px;top:2450px;background:linear-gradient(135deg,#5a5c60,#35373b)">
  <svg class="play" viewBox="0 0 64 64"><circle cx="32" cy="32" r="29" fill="none" stroke="#fff" stroke-width="3"/><path d="M26 20l18 12-18 12z" fill="#fff"/></svg>
</div>
<article class="card" style="left:118px;top:2515px"><h3>Consectetuer <b>Adipiscing</b></h3><div class="bar"></div><p>Lorem ipsum dolor sit amet, consectetuer adipiscing elit, sed diam nonummy nibh euismod tincidunt ut laoreet dolore magna aliquam erat volutpat. Ut wisi enim ad minim veniam, quis nostrud exerci tation ullamcorper suscipit lobortis nisl ut aliquip ex ea commodo consequat. Duis autem vel eum iriure dolor in hendrerit in vulputate ve</p></article>

<section class="expertise">
  <h2 class="heading">My <b>Expertise</b></h2>
  <div class="rule"></div>
  <div class="expertise-copy">
    <p>Lorem ipsum dolor sit amet, consectetuer adipiscing elit, sed diam nonummy nibh euismod tincidunt ut laoreet dolore magna aliquam erat volutpat. Ut wisi enim ad minim veniam, quis nostrud exerci tation ullamcorper.</p>
    <ul>
      <li>Consectetuer adipiscing elitsed diam nonummy nibh euismod</li>
      <li>Tincidunt ut laoreet dolore magna aliquam erat volutpat.</li>
      <li>Utwisi enim minim veniam, nostrud exerci tation ullamcorper.</li>
      <li>Utwisi enim minim veniam, nostrud exerci tation ullamcorper.</li>
    </ul>
  </div>
  <div class="photo" role="img" aria-label="Portrait of the recruiter in a grey suit" style="left:742px;top:97px;width:358px;height:330px;background:linear-gradient(180deg,#c7cbd0 0%,#6f747b 60%,#4a4e55 100%)"></div>
</section>

<section class="gallery">
  <h2>DIAM NONUMMY</h2>
  <div class="rule"></div>
  <svg class="arrow" style="left:44px" viewBox="0 0 20 28"><path d="M15 3L5 14l10 11" stroke="#fff" stroke-width="3" fill="none"/></svg>
  <svg class="arrow" style="left:1136px" viewBox="0 0 20 28"><path d="M5 3l10 11L5 25" stroke="#fff" stroke-width="3" fill="none"/></svg>
  <div class="tile" style="left:100px"><div class="photo" role="img" aria-label="Photo: team seated at a meeting table" style="background:linear-gradient(135deg,#d9dde2,#8e98a4)"></div><h4>TATION ULLAMCORPER</h4><p>Lorem ipsum dolor, consectetuer adipiscing sed diam nonummy</p></div>
  <div class="tile" style="left:353px"><div class="photo" role="img" aria-label="Photo: colleagues in conversation" style="background:linear-gradient(135deg,#b8c0c9,#5e6670)"></div><h4>TATION ULLAMCORPER</h4><p>Lorem ipsum dolor, consectetuer adipiscing sed diam nonummy</p></div>
  <div class="tile" style="left:606px"><div class="photo" role="img" aria-label="Photo: handshake at a desk" style="background:linear-gradient(135deg,#e3e6ea,#9aa3ad)"></div><h4>TATION ULLAMCORPER</h4><p>Lorem ipsum dolor, consectetuer adipiscing sed diam nonummy</p></div>
  <div class="tile" style="left:860px"><div class="photo" role="img" aria-label="Photo: business people standing together" style="background:linear-gradient(135deg,#dfe2e6,#7d858f)"></div><h4>TATION ULLAMCORPER</h4><p>Lorem ipsum dolor, consectetuer adipiscing sed diam nonummy</p></div>
</section>

<section class="inquiry">
  <h2 class="heading">A Question? <b>Quick Inquiry?</b></h2>
  <p class="lead">Just complete the below form and let us know how we can help you and also how we can reach you.</p>
  <div class="info" style="top:197px"><svg width="16" height="22" viewBox="0 0 16 22"><path d="M8 0a8 8 0 0 1 8 8c0 6-8 14-8 14S0 14 0 8a8 8 0 0 1 8-8z" fill="#2b58a5"/><circle cx="8" cy="8" r="3" fill="#fff"/></svg>48, Harrow Lane, Eastfield - 204518</div>
  <div class="info" style="top:250px"><svg width="18" height="18" viewBox="0 0 24 24"><path fill="#2b58a5" d="M6.6 10.8a15 15 0 0 0 6.6 6.6l2.2-2.2a1 1 0 0 1 1-.25 11.4 11.4 0 0 0 3.6.57 1 1 0 0 1 1 1V20a1 1 0 0 1-1 1A17 17 0 0 1 3 4a1 1 0 0 1 1-1h3.5a1 1 0 0 1 1 1c0 1.25.2 2.45.57 3.6a1 1 0 0 1-.25 1z"/></svg>(014) 5550192</div>
  <div class="info" style="top:297px"><svg width="18" height="14" viewBox="0 0 26 20"><rect x="1" y="1" width="24" height="18" rx="2" fill="#2b58a5"/><path d="M2 3l11 8 11-8" stroke="#fff" stroke-width="2" fill="none"/></svg>info@marlowevantrees.com</div>
  <div class="field" style="top:56px;height:38px">Name</div>
  <div class="field" style="top:108px;height:38px">Email</div>
  <div class="field" style="top:156px;height:40px">Phone</div>
  <div class="field" style="top:210px;height:83px">Message</div>
  <button class="submit">SUBMIT</button>
</section>

<footer class="site-footer">
  <p class="copy">Copyright © 2017 <b>MARLOWE VANTREES</b>. All Rights Reserved.</p>
  <div class="follow">Follow Us <i></i><i></i><i></i><i></i></div>
</footer>

</body>
</html>
```